Bluefork Conditioning OVR needs a website

We need a website design for Bluefork Conditioning. A sports performance training facility located in san juan capistrano. We train everyone from kids through professional athletes. We would need an info page explaining what we do and different options, staff page, testimonials page, contact page, etc.
http://www.tamblinstrength.com
http://kmwtraining.com/team/
Something similar to those ^ Thats kind of the company we are trying to emulate

athletes; specifically baseball and softball players

Training

5+ page

Serif

• home page, Training options page, staff, testimonial page, contact,
• a page for a blog and a page for videos. a spot for news updates on our clients on the home page

```html
<!DOCTYPE html>
<html lang="en">
<head>
<meta charset="utf-8">
<title>Bluefork Conditioning – Youth Athletic Training Centers</title>
<link href="https://fonts.googleapis.com/css2?family=Roboto:wght@300;400;500&display=swap" rel="stylesheet">
<style>
:root{
  --red:#e23a3f;
  --ink:#333333;
  --muted:#777777;
  --rule:#dddddd;
  --panel:#f2f2f2;
  --white:#ffffff;
}
*{box-sizing:border-box;margin:0;padding:0}
html,body{width:1200px;height:5000px;overflow:hidden}
body{position:relative;background:var(--white);font-family:"Roboto",Arial,sans-serif;color:var(--ink);font-weight:300}
.section{position:absolute;left:0;width:1200px}
.abs{position:absolute}
.title{position:absolute;left:0;width:1200px;text-align:center;color:var(--red);font-size:27px;font-weight:300}
.lede{position:absolute;left:250px;width:700px;text-align:center;font-size:14px;line-height:22px;color:var(--ink)}
.btn{position:absolute;border:1.5px solid var(--red);color:var(--red);font-size:13px;font-weight:400;display:flex;align-items:center;justify-content:center;background:var(--white)}
.photo{position:absolute}
.label{position:absolute;text-align:center;font-size:14px;font-weight:500;letter-spacing:.5px}

/* header */
.hero{top:0;height:717px;background:var(--white)}
.brand{position:absolute;left:133px;top:34px;display:flex;align-items:center;gap:12px}
.brand-mark{width:40px;height:40px;background:var(--red)}
.brand-name{font-size:34px;font-weight:500;color:var(--ink);line-height:1}
.call{position:absolute;left:705px;top:18px;display:flex;gap:10px;align-items:center}
.call-icon{width:34px;height:34px;border:1px solid var(--rule);border-radius:50%;display:flex;align-items:center;justify-content:center}
.call small{display:block;font-size:12px;color:var(--ink)}
.call strong{display:block;font-size:17px;font-weight:400;color:var(--red)}
.franchise{left:925px;top:22px;width:140px;height:34px;border-color:var(--ink);color:var(--ink);font-size:12px}
.nav{position:absolute;top:82px;left:507px;display:flex;gap:30px;font-size:13px;font-weight:400;align-items:center}
.nav .current{border:1.5px solid var(--red);color:var(--red);padding:6px 10px}
.hero-heading{position:absolute;left:133px;top:300px;font-size:46px;line-height:58px;font-weight:300}
.hero-photo{left:520px;top:115px;width:355px;height:565px;background:linear-gradient(180deg,#eaeaea,#c9c9c9)}
.dots{position:absolute;left:133px;top:596px;display:flex;gap:14px}
.dots span{width:20px;height:20px;border-radius:50%;border:1.5px solid #cccccc}
.dots span.on{border-color:#999}

/* pillars */
.pillars{top:717px;height:533px;background:var(--panel)}
.mission{left:160px;top:63px;width:345px;height:68px;border:1.5px solid var(--red);background:var(--white);padding:12px 16px;font-size:11px;line-height:17px;color:var(--muted)}
.pillar-label{position:absolute;font-size:15px;font-weight:400}

/* welcome */
.welcome{top:1250px;height:617px}
.program-photo{top:200px;width:285px;height:265px}

/* steps */
.steps{top:1867px;height:950px;background:var(--panel)}
.step-text{position:absolute;left:450px;width:300px;text-align:center;font-size:14px;line-height:22px;font-weight:400}

/* video */
.video{top:2817px;height:533px}
.video-card{left:705px;top:88px;width:362px;height:385px;border:1px solid var(--rule);background:var(--white)}
.video-card h3{position:absolute;left:70px;top:145px;font-size:15px;font-weight:400}
.video-card p{position:absolute;left:70px;top:178px;width:255px;font-size:12px;line-height:20px;color:var(--muted)}

/* news */
.news{top:3350px;height:500px;background:var(--panel)}
.news-card{position:absolute;top:140px;width:294px;height:300px;border:1px solid var(--rule);background:var(--panel)}
.news-card h3{position:absolute;left:70px;top:40px;width:200px;font-size:15px;font-weight:400;line-height:22px}
.news-card p{position:absolute;left:70px;top:110px;width:200px;font-size:12px;line-height:19px;color:var(--muted);text-align:justify}
.news-card svg{position:absolute;left:22px;top:46px}

/* sports */
.sports{top:3850px;height:633px}
.sport-photo{top:212px;width:287px;height:240px}

/* franchise */
.cta{top:4483px;height:234px;background:var(--panel)}

/* footer */
.footer{top:4717px;height:283px;background:var(--white)}
.footer h4{position:absolute;font-size:12px;font-weight:500;letter-spacing:.5px}
.footer ul{position:absolute;list-style:none;font-size:12px;line-height:20px;color:var(--muted)}
.social{position:absolute;left:910px;top:97px;display:flex;gap:8px}
.social span{width:30px;height:30px;border-radius:50%;background:var(--red)}
.social span:nth-child(1){background:#3b5998}
.social span:nth-child(2){background:#4aa8e8}
.social span:nth-child(3){background:#d64a3b}
.social span:nth-child(4){background:#2a77b0}
</style>
</head>
<body>

<header class="section hero">
  <div class="brand"><span class="brand-mark"></span><span class="brand-name">Bluefork</span></div>
  <div class="call">
    <span class="call-icon">
      <svg width="16" height="16" viewBox="0 0 24 24"><path d="M6.6 10.8a15 15 0 0 0 6.6 6.6l2.2-2.2c.3-.3.7-.4 1-.2 1.1.4 2.3.6 3.6.6.6 0 1 .4 1 1V20c0 .6-.4 1-1 1A17 17 0 0 1 3 4c0-.6.4-1 1-1h3.5c.6 0 1 .4 1 1 0 1.3.2 2.5.6 3.6.1.3 0 .7-.2 1z" fill="#999"/></svg>
    </span>
    <span><small>Call us</small><strong>1 - 800 - 555 - 0142</strong></span>
  </div>
  <div class="btn franchise">OWN A FRANCHISE</div>
  <nav class="nav">
    <span class="current">Home</span><span>About us</span><span>Training Options</span><span>Staff</span><span>Testimonials</span><span>Contact us</span>
  </nav>
  <h1 class="hero-heading" style="font-weight:300">Youth Athletic<br>Training Centers</h1>
  <div class="photo hero-photo" role="img" aria-label="Athlete lifting a loaded barbell in a deadlift stance"></div>
  <div class="dots"><span></span><span class="on"></span><span></span><span></span></div>
</header>

<section class="section pillars">
  <div class="abs mission">We are dedicated in making a difference in every athlete's life, through athletic training programs that we design.</div>
  <svg class="abs" style="left:0;top:0" width="1200" height="533">
    <line x1="505" y1="97" x2="550" y2="97" stroke="#e23a3f" stroke-width="1.5"/>
    <line x1="600" y1="148" x2="600" y2="208" stroke="#999" stroke-width="1.5"/>
    <line x1="600" y1="308" x2="600" y2="373" stroke="#999" stroke-width="1.5"/>
    <circle cx="600" cy="98" r="50" fill="#fff" stroke="#999" stroke-width="1.5"/>
    <circle cx="600" cy="258" r="50" fill="#fff" stroke="#999" stroke-width="1.5"/>
    <circle cx="600" cy="423" r="50" fill="#fff" stroke="#999" stroke-width="1.5"/>
    <path d="M580 82 h22 l8 8 v14 h-30z M588 94 h14 M588 100 h10" fill="none" stroke="#e23a3f" stroke-width="2"/>
    <path d="M578 248 h44 M585 240 v16 M615 240 v16 M592 262 h16 v18 h-16z" fill="none" stroke="#555" stroke-width="2"/>
    <path d="M586 410 h28 M592 404 v38 M608 404 v38 M588 428 h24" fill="none" stroke="#555" stroke-width="2"/>
  </svg>
  <span class="pillar-label" style="left:680px;top:87px;color:var(--red)">Speed</span>
  <span class="pillar-label" style="left:478px;top:249px">Power</span>
  <span class="pillar-label" style="left:680px;top:414px">Core</span>
</section>

<section class="section welcome">
  <h2 class="title" style="top:57px">Welcome to our site</h2>
  <p class="lede" style="left:220px;width:760px;top:105px">Welcome to Bluefork Conditioning Youth Athletic Training Center, where our goal is to transform you into the best young athlete you can be. No matter the sport, no matter your skill, Bluefork will make you a better athlete FIRST and then work on your sports specific skills.</p>
  <div class="photo program-photo" style="left:133px;background:linear-gradient(160deg,#7a3a3a,#2c2c2c)" role="img" aria-label="Two athletes training together on turf in the gym"></div>
  <div class="photo program-photo" style="left:457px;background:linear-gradient(160deg,#6c6c6c,#3a5a3a)" role="img" aria-label="Coach working one-on-one with a hitter"></div>
  <div class="photo program-photo" style="left:780px;background:linear-gradient(160deg,#8a2a2a,#333)" role="img" aria-label="Team of young athletes training as a group"></div>
  <span class="label" style="left:133px;width:285px;top:495px">SEMI-PRIVATE</span>
  <span class="label" style="left:457px;width:285px;top:495px">ONE-ON-ONE</span>
  <span class="label" style="left:780px;width:285px;top:495px">TEAM / GROUP</span>
  <div class="btn" style="left:217px;top:525px;width:116px;height:38px">Find Out More</div>
  <div class="btn" style="left:541px;top:525px;width:116px;height:38px">Find Out More</div>
  <div class="btn" style="left:864px;top:525px;width:116px;height:38px">Find Out More</div>
</section>

<section class="section steps">
  <h2 class="title" style="top:70px">Let's Get Started!</h2>
  <p class="lede" style="top:103px">Becoming a member at Bluefork is as easy as 1, 2, 3!</p>
  <svg class="abs" style="left:0;top:0" width="1200" height="950">
    <polyline points="540,192 560,186 580,194 600,184 620,192 640,186 660,196" fill="none" stroke="#e23a3f" stroke-width="2"/>
    <circle cx="540" cy="192" r="3" fill="#e23a3f"/><circle cx="600" cy="184" r="3" fill="#e23a3f"/><circle cx="660" cy="196" r="3" fill="#e23a3f"/>
    <path d="M395 250 Q340 330 400 410" fill="none" stroke="#555" stroke-width="1.5" stroke-dasharray="5 5"/>
    <path d="M396 402 l4 8 l-9 -1" fill="none" stroke="#555" stroke-width="1.5"/>
    <path d="M585 330 a18 18 0 0 1 30 0" fill="none" stroke="#e23a3f" stroke-width="2"/>
    <line x1="600" y1="330" x2="608" y2="318" stroke="#e23a3f" stroke-width="2"/>
    <path d="M800 430 Q860 510 800 585" fill="none" stroke="#555" stroke-width="1.5" stroke-dasharray="5 5"/>
    <path d="M806 578 l-6 7 l-2 -9" fill="none" stroke="#555" stroke-width="1.5"/>
    <rect x="582" y="525" width="36" height="26" fill="none" stroke="#e23a3f" stroke-width="2"/>
    <circle cx="592" cy="536" r="4" fill="none" stroke="#e23a3f" stroke-width="1.5"/>
    <line x1="600" y1="533" x2="612" y2="533" stroke="#e23a3f" stroke-width="1.5"/>
    <line x1="600" y1="541" x2="612" y2="541" stroke="#e23a3f" stroke-width="1.5"/>
    <line x1="596" y1="525" x2="596" y2="519" stroke="#e23a3f" stroke-width="2"/>
  </svg>
  <p class="step-text" style="top:235px">Come in today for a<br>Free Bluefork Athletic Evaluation</p>
  <p class="step-text" style="top:368px">Meet with a Sports<br>Performance Specialist</p>
  <p class="step-text" style="top:600px">Get your Membership!</p>
  <div class="btn" style="left:500px;top:788px;width:200px;height:40px">Sign up for a Free Week!</div>
</section>

<section class="section video">
  <h2 class="title" style="top:40px">Who is Bluefork in under 3 minutes</h2>
  <div class="photo" style="left:133px;top:88px;width:572px;height:385px;background:linear-gradient(180deg,#8f8f8f 0%,#5a5a5a 55%,#8a1f24 100%)" role="img" aria-label="Young athletes running cone drills on red turf in the training center"></div>
  <div class="abs video-card">
    <h3>H.I.I.T</h3>
    <p>The HIIT program is designed to prepare an athlete by training at a faster pace than they would experience in an actual game. Just as the name implies, this High Intensity Interval Training program...</p>
    <div class="btn" style="left:70px;top:315px;width:110px;height:38px">Watch Now</div>
    <svg class="abs" style="left:290px;top:355px" width="50" height="24"><path d="M12 4 L4 12 L12 20 M36 4 L44 12 L36 20" fill="none" stroke="#999" stroke-width="1.5"/></svg>
  </div>
</section>

<section class="section news">
  <h2 class="title" style="top:57px">Latest News</h2>
  <article class="news-card" style="left:133px">
    <svg width="14" height="24"><path d="M2 2 L12 12 L2 22" fill="none" stroke="#999" stroke-width="1.5"/></svg>
    <h3>Partnership With Terraflex Flooring</h3>
    <p>Terraflex – Advanced Exercise and Bluefork Athletic Announce Partnership to furnish all Youth Athletic Training Centers with Terraflex Flooring Nationwide.</p>
    <div class="btn" style="left:70px;top:245px;width:95px;height:34px">Read More</div>
  </article>
  <article class="news-card" style="left:453px">
    <svg width="14" height="24"><path d="M2 2 L12 12 L2 22" fill="none" stroke="#999" stroke-width="1.5"/></svg>
    <h3>The importance of staying hydrated!</h3>
    <p>Staying hydrated while playing your sport, or in your daily workouts, is of the upmost importance.</p>
    <div class="btn" style="left:70px;top:245px;width:95px;height:34px">Read More</div>
  </article>
  <article class="news-card" style="left:773px">
    <svg width="14" height="24"><path d="M2 2 L12 12 L2 22" fill="none" stroke="#999" stroke-width="1.5"/></svg>
    <h3>Partnership To Bring Pro-Level Training Nationwide</h3>
    <p>Youth athletic training centers across the country now offering same human performance and training platform used by professional and college athletes.</p>
    <div class="btn" style="left:70px;top:245px;width:95px;height:34px">Read More</div>
  </article>
</section>

<section class="section sports">
  <h2 class="title" style="top:83px">Multi - Sport Training</h2>
  <p class="lede" style="left:230px;width:740px;top:125px">At Bluefork, no matter the sport, no matter the skill, we will focus on making you a better all-around athlete in your chosen sport. Click your favorite sport below to find out more information.</p>
  <div class="photo sport-photo" style="left:133px;background:linear-gradient(180deg,#6f8f4f,#3f6a2f)" role="img" aria-label="Field hockey players competing for the ball"></div>
  <div class="photo sport-photo" style="left:457px;background:linear-gradient(180deg,#9ab07a,#c8a878)" role="img" aria-label="Young baseball batter at the plate"></div>
  <div class="photo sport-photo" style="left:780px;background:linear-gradient(180deg,#7aa05a,#4a7a3a)" role="img" aria-label="Youth soccer players chasing the ball"></div>
  <span class="label" style="left:133px;width:287px;top:483px">HOCKEY</span>
  <span class="label" style="left:457px;width:287px;top:483px">BASEBALL</span>
  <span class="label" style="left:780px;width:287px;top:483px">SOCCER</span>
  <div class="btn" style="left:532px;top:538px;width:136px;height:40px">Read More All</div>
</section>

<section class="section cta">
  <h2 class="title" style="top:70px">Want to own a Bluefork training center?</h2>
  <div class="btn" style="left:532px;top:133px;width:136px;height:40px">Find Out More</div>
</section>

<footer class="section footer">
  <div class="abs" style="left:133px;top:92px;display:flex;align-items:center;gap:10px">
    <span style="width:30px;height:30px;background:var(--red)"></span>
    <span style="font-size:26px;font-weight:500">Bluefork</span>
  </div>
  <p class="abs" style="left:133px;top:195px;font-size:11px;color:var(--muted)">Copyrights © 2016 All Rights Reserved</p>
  <h4 style="left:490px;top:62px">CONTACT US</h4>
  <ul style="left:490px;top:90px"><li>Arizona</li><li>Colorado</li><li>California</li><li>Northern region</li><li>Texas</li></ul>
  <h4 style="left:710px;top:62px">MENU</h4>
  <ul style="left:710px;top:90px"><li>Home</li><li>About us</li><li>Training Options</li><li>Staff</li><li>Testimonials</li><li>Contact us</li></ul>
  <h4 style="left:910px;top:62px">FOLLOW US</h4>
  <div class="social"><span></span><span></span><span></span><span></span></div>
</footer>

</body>
</html>
```